Fast Business Card Project

I need a business card with the name RENATO DUARTE stylized on one side and my email on the other (renatocosta4711@mailnova.com)

Industry/Entity Type

Business

Contact Information for Business Card

www.trilhamar.com.br

```html
<!DOCTYPE html>
<html lang="en">
<head>
<meta charset="utf-8">
<title>Renato Duarte – Business Card</title>
<link rel="stylesheet" href="https://fonts.googleapis.com/css2?family=Ubuntu:wght@500;700&display=swap">
<style>
  :root {
    --canvas: #ffffff;
    --card: #3e454d;
    --mark-tone: #737880;
    --ink-light: #ebe7e3;
    --accent: #d9262b;
    --shadow: rgba(0, 0, 0, 0.45);
  }
  html, body {
    margin: 0;
    padding: 0;
    width: 1200px;
    height: 1000px;
    overflow: hidden;
    background: var(--canvas);
    font-family: "Ubuntu", sans-serif;
  }
  .sheet {
    position: relative;
    width: 1200px;
    height: 1000px;
  }
  .card {
    position: absolute;
    width: 601px;
    height: 343px;
    background: var(--card);
    overflow: hidden;
  }
  .card--front { left: 86px; top: 75px; }
  .card--back { left: 510px; top: 587px; height: 344px; }

  .brand {
    position: absolute;
    left: 0;
    right: 0;
    top: 82px;
    display: flex;
    justify-content: center;
    align-items: center;
    gap: 10px;
  }
  .brand__dot {
    width: 14px;
    height: 14px;
    border-radius: 50%;
    background: var(--accent);
  }
  .brand__name {
    font-weight: 700;
    font-size: 60px;
    line-height: 1;
    color: var(--ink-light);
  }
  .card__name {
    position: absolute;
    left: 0;
    right: 0;
    top: 182px;
    margin: 0;
    text-align: center;
    font-weight: 500;
    font-size: 44px;
    letter-spacing: 0.5px;
    color: var(--ink-light);
    text-shadow: 2px 3px 4px var(--shadow);
  }

  .card__monogram {
    position: absolute;
    left: 18px;
    top: 20px;
    font-weight: 700;
    font-size: 260px;
    line-height: 1;
    color: var(--mark-tone);
  }
  .card__email {
    position: absolute;
    left: 128px;
    top: 286px;
    margin: 0;
    font-weight: 500;
    font-size: 22px;
    color: var(--ink-light);
    text-shadow: 1px 2px 3px var(--shadow);
  }
</style>
</head>
<body>
  <main class="sheet">
    <section class="card card--front" aria-label="Card front">
      <div class="brand">
        <span class="brand__dot"></span>
        <span class="brand__name">RD</span>
      </div>
      <h1 class="card__name">RENATO DUARTE</h1>
    </section>

    <section class="card card--back" aria-label="Card back">
      <div class="card__monogram" aria-hidden="true">RD</div>
      <p class="card__email">renatocosta4711@mailnova.com</p>
    </section>
  </main>
</body>
</html>
```